Webdesign für Vernetzung christlicher Geschäftsleute
Zielgruppe
Die Vereinigung KRTWLE bezweckt die Vernetzung christlicher Geschäftsleute und die Verbreitung von Biblisch fundierten ethischen Geschäftsprinzipien. Die Zielgruppe umfasst Unternehmer und Verantwortungsträger aus Wirtschaft und Politik.
Aufgabenstellung
Ich suche einen Designer, welcher sich ernsthaft mit den Anforderungen und dem Design auseinandersetzt und eine Individuelle Lösung gestaltet.
Das Logo sowie ein unverbindlicher Vorschlag für die Strukturierung liegen bei.
Bitte keine 08/15 Business Stock Fotos (Händeschütteln, Meetings, Präsentationen).
Das Design soll folgende Seiten beinhalten (Beschreibung folgt):
- Startseite
- Standardseite (Titel, Text mit Bildern)
- Event-Detail Seite (Titel, Ort, Datum, ev. Foto, Beschreibungstext, ev. Map)
- Chapter Startseite
Die bestehende Webseite ist kein Massstab ;).

```html
<!DOCTYPE html>
<html lang="de">
<head>
<meta charset="utf-8">
<title>KRTWLE – Webdesign</title>
<link href="https://fonts.googleapis.com/css2?family=Open+Sans:wght@400;600;700&family=Playfair+Display:wght@400&display=swap" rel="stylesheet">
<style>
  :root {
    --stage: #ececec;
    --paper: #ffffff;
    --ink: #111111;
    --accent: #b3122e;
    --muted: #444444;
    --snow-light: #f4f3f3;
    --snow-mid: #c9c6c7;
    --rock: #6b6868;
  }
  * { margin: 0; padding: 0; box-sizing: border-box; }
  html, body { width: 1200px; height: 844px; overflow: hidden; }
  body {
    background: var(--stage);
    font-family: "Open Sans", Arial, sans-serif;
    color: var(--ink);
    position: relative;
  }

  /* ---------- Desktop artboard ---------- */
  .desktop {
    position: absolute; left: 30px; top: 190px;
    width: 820px; height: 460px;
    background: var(--paper);
    overflow: hidden;
    box-shadow: 0 2px 14px rgba(0,0,0,.12);
  }
  .brand {
    position: absolute; display: flex; align-items: center; gap: 8px;
    font-weight: 700; color: var(--ink); letter-spacing: .04em;
  }
  .brand-dot { border-radius: 50%; background: var(--accent); flex: none; }
  .desktop .brand { left: 70px; top: 44px; font-size: 18px; }
  .desktop .brand-dot { width: 22px; height: 22px; }

  .main-nav { position: absolute; top: 56px; left: 0; width: 100%; }
  .main-nav a {
    position: absolute; font-size: 11.5px; font-weight: 600;
    color: var(--ink); text-decoration: none; letter-spacing: .02em;
  }
  .main-nav a.is-active::after {
    content: ""; position: absolute; left: -2px; right: -2px; bottom: -5px;
    height: 2px; background: var(--accent);
  }

  .hero-photo {
    position: absolute;
    background:
      radial-gradient(ellipse 55% 40% at 45% 45%, var(--rock) 0%, rgba(107,104,104,.45) 40%, rgba(255,255,255,0) 75%),
      linear-gradient(180deg, #dcd9da 0%, #eeecec 40%, var(--snow-light) 70%, #fbfafa 100%);
  }
  .desktop .hero-photo {
    left: 194px; top: 110px; width: 512px; height: 283px;
    box-shadow: 0 4px 14px rgba(0,0,0,.18);
  }
  .chapter-toggle {
    position: absolute; display: flex; align-items: center;
    font-weight: 600; color: var(--ink);
  }
  .desktop .chapter-toggle { right: 14px; top: 14px; font-size: 11.5px; gap: 8px; }

  .headline { position: absolute; font-weight: 700; color: var(--ink); }
  .headline span {
    display: table; background: var(--paper);
    padding: 0 6px 0 0;
  }
  .desktop .headline { left: 124px; top: 178px; font-size: 29px; line-height: 38.5px; letter-spacing: .01em; }

  .section-label {
    position: absolute; font-weight: 600; color: var(--accent); letter-spacing: .02em;
  }
  .desktop .section-label { font-size: 11.5px; top: 436px; }

  /* ---------- Mobile artboard ---------- */
  .mobile {
    position: absolute; left: 880px; top: 152px;
    width: 300px; height: 540px;
    background: var(--paper);
    overflow: hidden;
    box-shadow: 0 2px 14px rgba(0,0,0,.12);
  }
  .mobile .brand { left: 14px; top: 18px; font-size: 11px; gap: 5px; }
  .mobile .brand-dot { width: 12px; height: 12px; }
  .menu-icon { position: absolute; right: 12px; top: 18px; }
  .mobile .hero-photo { left: 0; top: 103px; width: 300px; height: 157px; }
  .mobile .headline { left: 24px; top: 64px; font-size: 13.5px; line-height: 20px; z-index: 1; }
  .mobile .headline span { padding: 0 5px 0 5px; margin-left: -5px; }
  .mobile .chapter-toggle { right: 10px; top: 110px; font-size: 7px; gap: 3px; }
  .mobile .section-label { font-size: 13.5px; left: 24px; }
  .body-copy {
    position: absolute; left: 24px; top: 302px; width: 250px;
    font-size: 7.6px; line-height: 12.3px; color: var(--muted);
  }
  .chapter-tile {
    position: absolute; top: 484px; height: 70px;
    background: linear-gradient(180deg, #f1f0f0 0%, #dedcdc 100%);
    box-shadow: 0 2px 8px rgba(0,0,0,.12);
    display: flex; justify-content: center; align-items: flex-end;
    font-family: "Playfair Display", Georgia, serif; font-size: 44px;
    color: var(--rock); line-height: 1;
  }
</style>
</head>
<body>

<section class="desktop" aria-label="Startseite Desktop">
  <div class="brand"><span class="brand-dot"></span>KRTWLE</div>

  <nav class="main-nav">
    <a href="#" class="is-active" style="left:427px">START</a>
    <a href="#" style="left:514px">ÜBER UNS</a>
    <a href="#" style="left:629px">KONTAKT</a>
  </nav>

  <div class="hero-photo" role="img" aria-label="Schneebedeckter Berggipfel im Nebel">
    <div class="chapter-toggle">CHAPTER
      <svg width="17" height="14" viewBox="0 0 17 14" aria-hidden="true">
        <rect y="0" width="17" height="2.6" fill="#111"/>
        <rect y="5.7" width="17" height="2.6" fill="#111"/>
        <rect y="11.4" width="17" height="2.6" fill="#111"/>
      </svg>
    </div>
  </div>

  <h1 class="headline">
    <span>SEIN</span><span>ZEICHEN</span><span>ÜBER UNS</span><span>IST LIEBE</span>
  </h1>

  <h2 class="section-label" style="left:109px">WILLKOMMEN</h2>
  <h2 class="section-label" style="left:545px">EVENTS</h2>
</section>

<section class="mobile" aria-label="Startseite Mobil">
  <div class="brand"><span class="brand-dot"></span>KRTWLE</div>
  <svg class="menu-icon" width="16" height="13" viewBox="0 0 16 13" aria-hidden="true">
    <rect y="0" width="16" height="2.4" fill="#111"/>
    <rect y="5.3" width="16" height="2.4" fill="#111"/>
    <rect y="10.6" width="16" height="2.4" fill="#111"/>
  </svg>

  <h1 class="headline">
    <span>SEIN ZEICHEN</span><span>ÜBER UNS IST</span><span>LIEBE</span>
  </h1>

  <div class="hero-photo" role="img" aria-label="Schneebedeckter Berggipfel im Nebel">
    <div class="chapter-toggle">CHAPTER
      <svg width="8" height="9" viewBox="0 0 8 9" aria-hidden="true">
        <path d="M1 1l3 3 3-3M1 5l3 3 3-3" fill="none" stroke="#b3122e" stroke-width="1.6"/>
      </svg>
    </div>
  </div>

  <h2 class="section-label" style="top:270px">WILLKOMMEN</h2>
  <p class="body-copy">Lorem ipsum dolor sit amet, consetetur sadipscing elitr, sed diam nonumy eirmod tempor invidunt ut labore et dolore magna aliquyam erat, sed diam voluptua. At vero eos et accusam et justo duo dolores et ea rebum. Stet clita kasd gubergren, no sea takimata sanctus est Lorem ipsum dolor sit amet. Lorem ipsum dolor sit amet, consetetur sadipscing elitr, sed diam nonumy eirmod tempor invidunt ut labore et dolore magna aliquyam erat, sed diam voluptua. At vero eos et accusam et justo duo dolores et ea rebum.</p>

  <h2 class="section-label" style="top:446px; left:31px">CHAPTERS</h2>
  <div class="chapter-tile" role="img" aria-label="Chapter I, verschneite Fläche" style="left:30px; width:107px">I</div>
  <div class="chapter-tile" role="img" aria-label="Chapter II, verschneite Fläche" style="left:168px; width:105px">II</div>
</section>

</body>
</html>
```